Need Letterhead Design & Matching Business Card

I have a logo that I love already. But the letterhead is less than appealing and boring. I'd like a design for my letterhead which I will match with business cards. Also, I'd like to have used fonts that are generally available, as my current letterhead uses a font named "SPACE" which nobody has unless they download it...so when a Word version is forwarded, it looks awful on the receiver's screed due to not having the font. That being said, modern is the look we like and are going for.

My business is "Halloran Brightmoor PC" - a law firm specializing in representing people who have suffered catastrophic injuries or death (plane, auto, train crashes etc.).

See attached letterhead, which has all of the pertinent information. My logo is also attached in various formats.

```html
<!DOCTYPE html>
<html lang="en">
<head>
<meta charset="utf-8">
<title>Halloran Brightmoor PC — Letterhead</title>
<link href="https://fonts.googleapis.com/css2?family=Arimo:ital,wght@0,400;0,700;1,400&display=swap" rel="stylesheet">
<style>
  :root {
    --ink: #000000;
    --paper: #ffffff;
  }
  html, body {
    margin: 0;
    padding: 0;
    width: 1200px;
    height: 1000px;
    overflow: hidden;
    background: var(--paper);
  }
  .letterhead {
    display: block;
    width: 1200px;
    height: 1000px;
  }
  .firm-name {
    font-family: "Arimo", Arial, sans-serif;
    font-weight: 700;
    font-size: 58px;
    fill: var(--ink);
  }
  .contact {
    font-family: "Arimo", Arial, sans-serif;
    font-size: 14px;
    font-weight: 700;
    fill: var(--ink);
  }
  .contact--web {
    font-weight: 400;
    font-style: italic;
  }
  .rule {
    fill: none;
    stroke: var(--ink);
    stroke-width: 4;
    stroke-linejoin: miter;
  }
  .center-block {
    fill: var(--ink);
  }
</style>
</head>
<body>
<svg class="letterhead" viewBox="0 0 1200 1000" xmlns="http://www.w3.org/2000/svg">
  <!-- Firm name split around the central block -->
  <text class="firm-name" x="98" y="496" textLength="395" lengthAdjust="spacing">HALLORAN</text>
  <rect class="center-block" x="522" y="437" width="156" height="155"/>
  <text class="firm-name" x="703" y="496" textLength="400" lengthAdjust="spacingAndGlyphs">BRIGHTMOOR PC</text>

  <!-- Left contact column -->
  <text class="contact" x="117" y="533">R. Idris Malvern, Esq. | President</text>
  <text class="contact" x="117" y="553">4200 Larkspur Ave. | suite 800</text>
  <text class="contact" x="117" y="573">Westbrook, CA 90418</text>

  <!-- Right contact column -->
  <text class="contact" x="1080" y="533" text-anchor="end">idris@halloranbrightmoor.com</text>
  <text class="contact contact--web" x="1080" y="553" text-anchor="end">www.halloranbrightmoor.com</text>
  <text class="contact" x="1080" y="573" text-anchor="end">Tel: (855) 555-0142</text>

  <!-- Base rule stepping up into the central block -->
  <polyline class="rule" points="98,598 500,598 523,580"/>
  <polyline class="rule" points="677,580 700,598 1102,598"/>
</svg>
</body>
</html>
```